Wedding Day Custom Wine Label - Tasmanian (Tamar Valley) wine

I am looking for a custom design that will be put on a wine label to commemorate a very good friend's wedding day.

We will need to be able to take the design and print it on to sticker labels that we can put on to wine bottles.

The bride and groom have asked for a simplistic label design (see example image attached). We need two labels. One for "Pinot Noir" wine and the other for "Chardonnay" wine. We would like the label to say:

The Hartwell's
Pinot Noir
2023
Tamar Valley

and for for the other wine variety:

The Hartwell's
Chardonnay
2023
Tamar Valley

smaller text below to say:

13.5% ALC/VOL 750ML
MEGAN & LIAM - 31.10.2024

I am happy to consider other variations - the bride & groom would prefer something minimalistic. Elegant and classy.

Target Market(s)

the bride & groom

Requirements
Must have
• Wedding date (31.10.2024). Wine type (Pinot Noir or Chardonnay).
Should not have
• images not essential

```html
<!DOCTYPE html>
<html lang="en">
<head>
<meta charset="utf-8">
<title>The Hartwell's Wedding Wine Labels</title>
<link rel="stylesheet" href="https://fonts.googleapis.com/css2?family=Bebas+Neue&display=swap">
<style>
  :root {
    --backdrop: #2c373c;
    --label-paper: #ffffff;
    --ink: #0d0d0d;
    --gold: #c4971c;
  }
  * { margin: 0; padding: 0; box-sizing: border-box; }
  html, body {
    width: 1200px;
    height: 584px;
    overflow: hidden;
    background: var(--backdrop);
  }
  .sheet {
    position: relative;
    width: 1200px;
    height: 584px;
    display: flex;
    justify-content: center;
    align-items: center;
    gap: 38px;
  }
  .wine-label {
    position: relative;
    width: 363px;
    height: 412px;
    background: var(--label-paper);
    color: var(--ink);
    font-family: "Bebas Neue", "Arial Narrow", sans-serif;
    text-align: center;
  }
  .couple-artwork {
    position: absolute;
    left: 113px;
    top: 15px;
    width: 136px;
    height: 138px;
    display: block;
  }
  .label-line {
    position: absolute;
    left: 0;
    right: 0;
    line-height: 1;
    transform: translateY(-50%);
    white-space: nowrap;
  }
  .family-name { top: 186px; font-size: 42px; }
  .variety     { top: 235px; font-size: 42px; }
  .vintage     { top: 274px; font-size: 42px; }
  .region      { top: 312px; font-size: 42px; letter-spacing: 0.5px; }
  .details     { top: 355px; font-size: 19px; }
  .dedication  { top: 379px; font-size: 19px; }
</style>
</head>
<body>
  <main class="sheet">
    <section class="wine-label wine-label--pinot">
      <svg class="couple-artwork" viewBox="0 0 136 138" role="img" aria-label="Gold silhouette illustration of a bride and groom beneath an arch of trees">
        <path d="M0 138 V40 Q0 0 40 0 H136 V138 Z" fill="var(--gold)"/>
      </svg>
      <p class="label-line family-name">The Hartwell's</p>
      <p class="label-line variety">Pinot Noir</p>
      <p class="label-line vintage">2023</p>
      <p class="label-line region">Tamar Valley</p>
      <p class="label-line details">13,5% ALC/VOL 750ML</p>
      <p class="label-line dedication">MEGAN &amp; LIAM - 31.10.2024</p>
    </section>

    <section class="wine-label wine-label--chardonnay">
      <svg class="couple-artwork" viewBox="0 0 136 138" role="img" aria-label="Gold silhouette illustration of a bride and groom beneath an arch of trees">
        <path d="M0 138 V40 Q0 0 40 0 H136 V138 Z" fill="var(--gold)"/>
      </svg>
      <p class="label-line family-name">The Hartwell's</p>
      <p class="label-line variety">Chardonnay</p>
      <p class="label-line vintage">2023</p>
      <p class="label-line region">Tamar Valley</p>
      <p class="label-line details">13,5% ALC/VOL 750ML</p>
      <p class="label-line dedication">MEGAN &amp; LIAM - 31.10.2024</p>
    </section>
  </main>
</body>
</html>
```